integrative health clinic-Medical massage, acupuncture, chiropractic

we like our logo, but are open to new ideas. We need a new card design. We have added chiropractic and acupuncture that we have put under the name of the business. We are an integrative medical clinic

Target Market(s)

General public, athletes

Contact Information for Business Card

Phone 5055583927
Fax 5055583926
Hours Monday-Friday 9-6
Saturday 10-6
The 20% can be smaller on the back

Colors
3176b5
0355a3

Requirements
Must have
• Logo but am open to ideas
Nice to have
• We are an integrated medical clinic but also want to be personable. We want the card fun and inviting

```html
<!DOCTYPE html>
<html lang="en">
<head>
<meta charset="utf-8">
<title>Evergreen Core Wellness – Business Card</title>
<link rel="stylesheet" href="https://fonts.googleapis.com/css2?family=Lato:wght@400;700&family=Cormorant+Garamond:ital,wght@1,500&display=swap">
<style>
  :root {
    --clinic-blue: #2c409c;
    --card-white: #ffffff;
    --ink: #1c1c1c;
    --backdrop: #5e5e5e;
  }
  * { box-sizing: border-box; margin: 0; padding: 0; }
  html, body {
    width: 1200px; height: 900px; overflow: hidden;
    background: var(--backdrop);
    font-family: "Lato", Arial, sans-serif;
  }
  .card-sheet {
    width: 1200px; height: 900px;
    display: flex; align-items: center; justify-content: center; gap: 40px;
  }
  .card {
    position: relative;
    width: 540px; height: 309px;
    overflow: hidden;
    box-shadow: 0 10px 28px rgba(0,0,0,0.35);
  }
  .card--front { background: var(--card-white); }
  .card--back { background: var(--clinic-blue); }

  .brand { position: absolute; top: 42px; left: 0; width: 100%; padding-left: 120px; }
  .brand__name {
    font-family: "Lato", Arial, sans-serif;
    font-weight: 700;
    font-size: 30px;
    letter-spacing: -0.4px;
    line-height: 1;
    white-space: nowrap;
  }
  .brand__line {
    display: flex; align-items: center; gap: 8px; margin-top: 6px; padding-left: 2px;
  }
  .brand__dot {
    width: 20px; height: 20px; border-radius: 50%; flex: none;
  }
  .brand__tagline {
    font-family: "Cormorant Garamond", Georgia, serif;
    font-style: italic; font-weight: 500;
    font-size: 17px; letter-spacing: 0.6px;
    white-space: nowrap;
  }

  .card--front .brand__name { color: var(--ink); }
  .card--front .brand__dot { background: var(--clinic-blue); }
  .card--front .brand__tagline { color: var(--ink); }

  .specialty-label {
    position: absolute; top: 150px; left: 170px;
    color: var(--clinic-blue); font-weight: 700; font-size: 17px;
  }
  .specialty-band {
    position: absolute; top: 182px; left: 0; width: 100%; height: 42px;
    background: var(--clinic-blue);
    color: var(--card-white);
    font-weight: 700; font-size: 24px;
    display: flex; align-items: center; padding-left: 60px;
    white-space: nowrap;
  }
  .contact {
    position: absolute; top: 244px; font-size: 20px; color: var(--ink);
    white-space: nowrap;
  }
  .contact__label { color: var(--clinic-blue); font-weight: 700; }
  .contact--phone { left: 26px; }
  .contact--fax { left: 290px; top: 264px; }

  .card--back .brand__name,
  .card--back .brand__tagline { color: var(--card-white); }
  .card--back .brand__dot { background: var(--card-white); }

  .hours-band {
    position: absolute; top: 160px; left: 0; width: 100%; height: 44px;
    background: var(--card-white);
    color: var(--clinic-blue);
    font-weight: 700; font-size: 21px; letter-spacing: 0.5px;
    display: flex; align-items: center; padding-left: 140px;
  }
  .hours-list {
    position: absolute; top: 214px; left: 120px;
    list-style: none; color: var(--card-white); font-size: 16px; line-height: 1.35;
  }
</style>
</head>
<body>
  <main class="card-sheet">
    <section class="card card--front" aria-label="Card front">
      <div class="brand">
        <div class="brand__name">Evergreen Core Wellness</div>
        <div class="brand__line">
          <span class="brand__dot"></span>
          <span class="brand__tagline">Integrative Medical Clinic</span>
        </div>
      </div>
      <p class="specialty-label">Specializing in:</p>
      <div class="specialty-band">Chiropractic and Acupuncture</div>
      <p class="contact contact--phone"><span class="contact__label">Phone:</span> 5055583927</p>
      <p class="contact contact--fax"><span class="contact__label">Fax:</span> 5055583926</p>
    </section>

    <section class="card card--back" aria-label="Card back">
      <div class="brand">
        <div class="brand__name">Evergreen Core Wellness</div>
        <div class="brand__line">
          <span class="brand__dot"></span>
          <span class="brand__tagline">Integrative Medical Clinic</span>
        </div>
      </div>
      <div class="hours-band">OPENING HOURS</div>
      <ul class="hours-list">
        <li>Monday-Friday 9am - 6pm,</li>
        <li>Saturday 10am - 6pm</li>
      </ul>
    </section>
  </main>
</body>
</html>
```